" Fazer o calendário de parede conforme o anexo abaixo sendo que a parte para fazer o cabeçalho tem que ter a medida 41cm de comprimento por 11,5cm de altura "

```html
<!DOCTYPE html>
<html lang="pt-BR">
<head>
<meta charset="UTF-8">
<title>Calendário 2026 – Verdejar Hortifruti</title>
<link href="https://fonts.googleapis.com/css2?family=Roboto+Slab:wght@600;700;800&family=Roboto:wght@400;500;700&display=swap" rel="stylesheet">
<style>
  :root{
    --green-dark:#1f6b3d;
    --green:#2a7a47;
    --green-light:#b9dcc3;
    --band:#eef0ee;
    --ink:#2b2b2b;
    --muted:#5f6b63;
    --red:#d6322a;
    --stage:#9b9b9b;
    --paper:#ffffff;
  }
  *{box-sizing:border-box;margin:0;padding:0}
  html,body{width:1200px;height:1200px;overflow:hidden}
  body{background:var(--stage);font-family:"Roboto",sans-serif;color:var(--ink);position:relative}
  .poster{position:absolute;left:192px;top:36px;width:816px;height:1140px;background:var(--paper);overflow:hidden}
  .top-strip{position:absolute;left:0;top:0;width:100%;height:40px;background:var(--green)}
  .brand{position:absolute;left:206px;top:56px;display:flex;align-items:center;gap:10px;white-space:nowrap}
  .brand-name{font-family:"Roboto Slab",serif;font-weight:800;font-size:29px;color:var(--green-dark);letter-spacing:.3px;line-height:1}
  .brand-dot{width:16px;height:16px;border-radius:50%;background:var(--red);flex:none}
  .address{position:absolute;left:548px;top:56px;width:230px;font-size:11px;line-height:16px;color:var(--muted);white-space:nowrap}
  .year{position:absolute;left:0;right:0;top:158px;display:flex;align-items:center;justify-content:center;gap:28px}
  .year-line{width:210px;height:3px;background:var(--green)}
  .year-num{font-family:"Roboto Slab",serif;font-weight:800;font-size:50px;color:var(--green-dark);line-height:1}
  .row-band{position:absolute;left:0;width:100%;height:186px;background:var(--band)}
  .month{position:absolute;width:196px}
  .month-name{font-family:"Roboto Slab",serif;font-weight:700;font-size:18px;color:var(--green-dark);text-align:center;height:24px;line-height:22px}
  .week-head{display:grid;grid-template-columns:repeat(7,1fr);background:var(--green-dark);color:#fff;font-size:10px;font-weight:700;height:17px;line-height:17px;text-align:center}
  .days{display:grid;grid-template-columns:repeat(7,1fr);grid-template-rows:repeat(6,17px);font-size:11px;text-align:center;line-height:17px;
    background:linear-gradient(to right,transparent 71.43%,var(--green-light) 71.43%)}
  .days span{display:flex;align-items:center;justify-content:center}
  .hol{position:relative}
  .hol::before{content:"";position:absolute;width:15px;height:15px;border-radius:50%;background:var(--green-light);border:1px solid var(--green);z-index:0;left:50%;top:50%;transform:translate(-50%,-50%)}
  .hol b{position:relative;z-index:1;font-weight:500}
  .note{font-size:7.5px;color:var(--muted);margin-top:5px;height:10px;white-space:nowrap;overflow:hidden}
  .c1{left:79px}.c2{left:317px}.c3{left:554px}
  .r1{top:228px}.r2{top:412px}.r3{top:598px}.r4{top:782px}
  .produce{position:absolute;left:0;bottom:0;width:100%;height:170px;
    background:linear-gradient(90deg,#e2873a 0%,#6f9a3c 18%,#f0b72f 32%,#e9e7d9 42%,#c9392b 52%,#86a94a 64%,#e6b53e 74%,#c6362c 84%,#3f6b32 100%)}
</style>
</head>
<body>
<main class="poster">
  <div class="top-strip"></div>
  <header class="brand">
    <span class="brand-dot"></span>
    <span class="brand-name">Verdejar Hortifruti</span>
  </header>
  <p class="address">Av. das Palmeiras, 512 | Jardim Aurora<br>Campo Grande | MS</p>

  <div class="year"><span class="year-line"></span><h1 class="year-num">2026</h1><span class="year-line"></span></div>

  <div class="row-band" style="top:402px"></div>

  <section class="month c1 r1"><h2 class="month-name">Janeiro</h2>
    <div class="week-head"><span>S</span><span>T</span><span>Q</span><span>Q</span><span>S</span><span>S</span><span>D</span></div>
    <div class="days"><span class="hol" style="grid-column-start:4"><b>1</b></span><span>2</span><span>3</span><span>4</span><span>5</span><span>6</span><span>7</span><span>8</span><span>9</span><span>10</span><span>11</span><span>12</span><span>13</span><span>14</span><span>15</span><span>16</span><span>17</span><span>18</span><span>19</span><span>20</span><span>21</span><span>22</span><span>23</span><span>24</span><span>25</span><span>26</span><span>27</span><span>28</span><span>29</span><span>30</span><span>31</span></div>
    <p class="note">01. Confraternização Universal</p></section>

  <section class="month c2 r1"><h2 class="month-name">Fevereiro</h2>
    <div class="week-head"><span>S</span><span>T</span><span>Q</span><span>Q</span><span>S</span><span>S</span><span>D</span></div>
    <div class="days"><span style="grid-column-start:7">1</span><span>2</span><span>3</span><span>4</span><span>5</span><span>6</span><span>7</span><span>8</span><span>9</span><span>10</span><span>11</span><span>12</span><span>13</span><span>14</span><span>15</span><span>16</span><span class="hol"><b>17</b></span><span>18</span><span>19</span><span>20</span><span>21</span><span>22</span><span>23</span><span>24</span><span>25</span><span>26</span><span>27</span><span>28</span></div>
    <p class="note">17. Carnaval</p></section>

  <section class="month c3 r1"><h2 class="month-name">Março</h2>
    <div class="week-head"><span>S</span><span>T</span><span>Q</span><span>Q</span><span>S</span><span>S</span><span>D</span></div>
    <div class="days"><span style="grid-column-start:7">1</span><span>2</span><span>3</span><span>4</span><span>5</span><span>6</span><span>7</span><span class="hol"><b>8</b></span><span>9</span><span>10</span><span>11</span><span>12</span><span>13</span><span>14</span><span>15</span><span>16</span><span>17</span><span>18</span><span>19</span><span>20</span><span>21</span><span>22</span><span>23</span><span>24</span><span>25</span><span>26</span><span>27</span><span>28</span><span>29</span><span>30</span><span>31</span></div>
    <p class="note">08. Dia Internacional da Mulher</p></section>

  <section class="month c1 r2"><h2 class="month-name">Abril</h2>
    <div class="week-head"><span>S</span><span>T</span><span>Q</span><span>Q</span><span>S</span><span>S</span><span>D</span></div>
    <div class="days"><span style="grid-column-start:3">1</span><span>2</span><span class="hol"><b>3</b></span><span>4</span><span class="hol"><b>5</b></span><span>6</span><span>7</span><span>8</span><span>9</span><span>10</span><span>11</span><span>12</span><span>13</span><span>14</span><span>15</span><span>16</span><span>17</span><span>18</span><span>19</span><span>20</span><span class="hol"><b>21</b></span><span>22</span><span>23</span><span>24</span><span>25</span><span>26</span><span>27</span><span>28</span><span>29</span><span>30</span></div>
    <p class="note">03. Sexta-feira Santa | 05. Páscoa | 21. Tiradentes</p></section>

  <section class="month c2 r2"><h2 class="month-name">Maio</h2>
    <div class="week-head"><span>S</span><span>T</span><span>Q</span><span>Q</span><span>S</span><span>S</span><span>D</span></div>
    <div class="days"><span class="hol" style="grid-column-start:5"><b>1</b></span><span>2</span><span>3</span><span>4</span><span>5</span><span>6</span><span>7</span><span>8</span><span>9</span><span class="hol"><b>10</b></span><span>11</span><span>12</span><span>13</span><span>14</span><span>15</span><span>16</span><span>17</span><span>18</span><span>19</span><span>20</span><span>21</span><span>22</span><span>23</span><span>24</span><span>25</span><span>26</span><span>27</span><span>28</span><span>29</span><span>30</span><span>31</span></div>
    <p class="note">01. Dia do Trabalho | 10. Dia das Mães</p></section>

  <section class="month c3 r2"><h2 class="month-name">Junho</h2>
    <div class="week-head"><span>S</span><span>T</span><span>Q</span><span>Q</span><span>S</span><span>S</span><span>D</span></div>
    <div class="days"><span>1</span><span>2</span><span>3</span><span class="hol"><b>4</b></span><span>5</span><span>6</span><span>7</span><span>8</span><span>9</span><span>10</span><span>11</span><span>12</span><span>13</span><span>14</span><span>15</span><span>16</span><span>17</span><span>18</span><span>19</span><span>20</span><span>21</span><span>22</span><span>23</span><span>24</span><span>25</span><span>26</span><span>27</span><span>28</span><span>29</span><span>30</span></div>
    <p class="note">04. Corpus Christi</p></section>

  <section class="month c1 r3"><h2 class="month-name">Julho</h2>
    <div class="week-head"><span>S</span><span>T</span><span>Q</span><span>Q</span><span>S</span><span>S</span><span>D</span></div>
    <div class="days"><span style="grid-column-start:3">1</span><span>2</span><span>3</span><span>4</span><span>5</span><span>6</span><span>7</span><span>8</span><span>9</span><span>10</span><span>11</span><span>12</span><span>13</span><span>14</span><span>15</span><span>16</span><span>17</span><span>18</span><span>19</span><span>20</span><span>21</span><span>22</span><span>23</span><span>24</span><span>25</span><span>26</span><span>27</span><span>28</span><span>29</span><span>30</span><span>31</span></div>
    <p class="note"></p></section>

  <section class="month c2 r3"><h2 class="month-name">Agosto</h2>
    <div class="week-head"><span>S</span><span>T</span><span>Q</span><span>Q</span><span>S</span><span>S</span><span>D</span></div>
    <div class="days"><span style="grid-column-start:6">1</span><span>2</span><span>3</span><span>4</span><span>5</span><span>6</span><span>7</span><span>8</span><span class="hol"><b>9</b></span><span>10</span><span>11</span><span>12</span><span>13</span><span>14</span><span>15</span><span>16</span><span>17</span><span>18</span><span>19</span><span>20</span><span>21</span><span>22</span><span>23</span><span>24</span><span>25</span><span>26</span><span>27</span><span>28</span><span>29</span><span>30</span><span>31</span></div>
    <p class="note">09. Dia dos Pais</p></section>

  <section class="month c3 r3"><h2 class="month-name">Setembro</h2>
    <div class="week-head"><span>S</span><span>T</span><span>Q</span><span>Q</span><span>S</span><span>S</span><span>D</span></div>
    <div class="days"><span style="grid-column-start:2">1</span><span>2</span><span>3</span><span>4</span><span>5</span><span>6</span><span class="hol"><b>7</b></span><span>8</span><span>9</span><span>10</span><span>11</span><span>12</span><span>13</span><span>14</span><span>15</span><span>16</span><span>17</span><span>18</span><span>19</span><span>20</span><span>21</span><span>22</span><span>23</span><span>24</span><span>25</span><span>26</span><span>27</span><span>28</span><span>29</span><span>30</span></div>
    <p class="note">07. Dia da Independência do Brasil</p></section>

  <section class="month c1 r4"><h2 class="month-name">Outubro</h2>
    <div class="week-head"><span>S</span><span>T</span><span>Q</span><span>Q</span><span>S</span><span>S</span><span>D</span></div>
    <div class="days"><span style="grid-column-start:4">1</span><span>2</span><span>3</span><span>4</span><span>5</span><span>6</span><span>7</span><span>8</span><span>9</span><span>10</span><span>11</span><span class="hol"><b>12</b></span><span>13</span><span>14</span><span class="hol"><b>15</b></span><span>16</span><span>17</span><span>18</span><span>19</span><span>20</span><span>21</span><span>22</span><span>23</span><span>24</span><span>25</span><span>26</span><span>27</span><span>28</span><span>29</span><span>30</span><span>31</span></div>
    <p class="note">12. N. Sra. Aparecida | 15. Dia do Professor</p></section>

  <section class="month c2 r4"><h2 class="month-name">Novembro</h2>
    <div class="week-head"><span>S</span><span>T</span><span>Q</span><span>Q</span><span>S</span><span>S</span><span>D</span></div>
    <div class="days"><span style="grid-column-start:7">1</span><span class="hol"><b>2</b></span><span>3</span><span>4</span><span>5</span><span>6</span><span>7</span><span>8</span><span>9</span><span>10</span><span>11</span><span>12</span><span>13</span><span>14</span><span>15</span><span>16</span><span>17</span><span>18</span><span>19</span><span class="hol"><b>20</b></span><span>21</span><span>22</span><span>23</span><span>24</span><span>25</span><span>26</span><span>27</span><span>28</span><span>29</span><span>30</span></div>
    <p class="note">02. Finados | 20. Consciência Negra</p></section>

  <section class="month c3 r4"><h2 class="month-name">Dezembro</h2>
    <div class="week-head"><span>S</span><span>T</span><span>Q</span><span>Q</span><span>S</span><span>S</span><span>D</span></div>
    <div class="days"><span style="grid-column-start:2">1</span><span>2</span><span>3</span><span>4</span><span>5</span><span>6</span><span>7</span><span>8</span><span>9</span><span>10</span><span>11</span><span>12</span><span>13</span><span>14</span><span>15</span><span>16</span><span>17</span><span>18</span><span>19</span><span>20</span><span>21</span><span>22</span><span>23</span><span>24</span><span class="hol"><b>25</b></span><span>26</span><span>27</span><span>28</span><span>29</span><span>30</span><span>31</span></div>
    <p class="note">25. Natal</p></section>

  <div class="produce" role="img" aria-label="Fotografia de legumes e verduras frescos: cenoura, brócolis, pimentão amarelo, tomates, milho e abobrinha"></div>
</main>
</body>
</html>
```